Pregnancy and Fertility Information Website

Hello Designers,
I need a website which provide tips and information about healthy and happy pregnancy. My website name is Lorvin medical.

The website should provide all the information needed throughout pregnancy and beyond ranging from pregnancy tracking tools and articles about common pregnancy concerns and what to expect during pregnancy,etc.
The details about first trimester, second trimester and third trimester should be highlighted in the website.

Top Navigation
Home, Fertility, Pregnancy basics, Articles, Tips and News

I'm looking for a simple and clean design which involves captivating images and colors but it shouldn't be crowded. The design must be professional and modern. An easy to navigate layout is a must.

Green, violet, blue and light yellow colors are my favorites but i'm open to other options.

Any questions. Kindly ask

Industry/Entity Type

Medical

```html
<!DOCTYPE html>
<html lang="en">
<head>
<meta charset="utf-8">
<title>Lorvin medical — Healthy and Happy Pregnancy</title>
<link rel="stylesheet" href="https://fonts.googleapis.com/css2?family=Roboto:ital,wght@0,300;0,400;0,500;0,700;1,300;1,400&family=Lato:wght@400;700&display=swap">
<style>
:root{
  --green:#86c043;
  --green-dark:#6fa832;
  --blue:#0c4a8e;
  --blue-deep:#083b74;
  --ink:#333a40;
  --text:#6c7277;
  --muted:#9aa0a4;
  --line:#e3e6e8;
  --mint:#f3faec;
  --white:#ffffff;
}
*{box-sizing:border-box;margin:0;padding:0}
html,body{width:1200px;height:3488px;overflow:hidden}
body{font-family:"Lato",Arial,sans-serif;color:var(--text);background:var(--white);position:relative}
section,header,footer{position:absolute;left:0;width:1200px}
.abs{position:absolute}
h2{font-family:"Roboto",Arial,sans-serif;font-weight:300;color:var(--ink)}
.accent{color:var(--green)}
.btn{display:inline-block;background:var(--green);color:var(--white);font-family:"Roboto",Arial,sans-serif;font-weight:500;font-size:12px;padding:6px 14px;border-radius:2px}

/* header */
.site-header{top:0;height:60px;background:var(--white)}
.brand{left:190px;top:14px;display:flex;align-items:center;gap:8px;font-family:"Roboto",Arial,sans-serif;font-weight:500;font-size:17px;color:var(--green)}
.brand-dot{width:30px;height:30px;border-radius:50%;background:var(--green)}
.main-nav{left:505px;top:0;display:flex;gap:24px;font-family:"Roboto",Arial,sans-serif;font-size:10.5px;font-weight:500;color:var(--blue);text-transform:uppercase}
.main-nav a{padding-top:26px;height:60px;text-decoration:none;color:inherit}
.main-nav a.active{color:var(--green);border-top:3px solid var(--green);padding-top:23px}
.header-tools{left:915px;top:22px;display:flex;gap:14px;align-items:center}
.tool-dot{width:10px;height:10px;border-radius:50%;background:var(--blue)}

/* hero */
.hero{top:60px;height:587px;background:linear-gradient(100deg,#8e8a82 0%,#b7aa9c 35%,#d2c6b8 60%,#a9a39b 100%)}
.hero-card{left:247px;top:205px;width:360px;height:175px;background:var(--green);padding:28px 28px;color:var(--white)}
.hero-card h1{font-family:"Roboto",Arial,sans-serif;font-weight:300;font-size:30px;line-height:1.05;margin-bottom:12px}
.hero-card p{font-size:12.5px;line-height:1.5}
.fold{position:absolute;right:0;top:0}
.hero-arrow{top:278px}
.hero-dots{left:564px;top:557px;display:flex;gap:9px}
.hero-dots span{width:7px;height:7px;border-radius:50%;background:rgba(255,255,255,.6)}
.hero-dots span.on{background:var(--green)}

/* welcome */
.welcome{top:647px;height:346px}
.welcome h2{left:190px;top:58px;font-size:37px}
.welcome h2 b{font-weight:500}
.lead{font-size:14.5px;line-height:1.55;color:var(--text)}
.welcome .lead{left:190px;top:110px;width:560px}
.trimester{top:187px;width:265px;display:flex;gap:16px}
.tri-num{flex:none;width:56px;height:56px;border-radius:50%;border:2px solid #c3c7ca;display:flex;align-items:center;justify-content:center;font-family:"Roboto",Arial,sans-serif;font-size:20px;color:var(--ink)}
.tri-num.alt{border-color:var(--green);background:#eef7e4;color:var(--green)}
.trimester h3{font-family:"Roboto",Arial,sans-serif;font-weight:500;font-size:14px;color:var(--ink);margin:10px 0 12px}
.trimester p{font-size:10.5px;line-height:1.55}
.trimester a{display:block;margin-top:10px;font-size:9.5px;color:var(--green);text-decoration:none}

/* trimester feature */
.feature{top:993px;height:417px;background:linear-gradient(90deg,#cfe3a4 0%,#e6edd5 40%,#d9e6b4 70%,#c6dd92 100%)}
.feature-photo{left:0;top:0;width:1200px;height:417px}
.notch{left:560px;top:-1px}
.feature-card{left:582px;top:84px;width:530px;height:253px;background:var(--blue);padding:34px 32px;color:var(--white)}
.feature-card h3{font-family:"Roboto",Arial,sans-serif;font-weight:400;font-size:24px;margin-bottom:14px}
.feature-card .intro{font-size:13px;line-height:1.5;margin-bottom:12px}
.feature-card .detail{font-size:10.5px;line-height:1.6;color:#b9cbe2;margin-bottom:16px}

/* advisors */
.advisors{top:1410px;height:440px}
.advisors h2{left:190px;top:68px;font-size:33px}
.advisors .lead{left:190px;top:118px;width:380px}
.checklist{left:190px;top:188px;list-style:none;font-size:11.5px;line-height:2.1}
.checklist li{display:block;white-space:nowrap}
.checklist svg{display:inline-block;vertical-align:middle;margin-right:12px}
.advisors .btn{left:190px;top:357px}
.advisors-photo{left:675px;top:44px;width:335px;height:337px;background:linear-gradient(180deg,#eef3f6 0%,#d8e2ea 100%)}

/* feedback */
.feedback{top:1850px;height:534px;background:var(--mint)}
.feedback h2{left:0;width:1200px;text-align:center;top:52px;font-size:33px}
.client-photo{left:205px;top:139px;width:218px;height:318px;background:linear-gradient(180deg,#e9eef0 0%,#2e343b 55%,#22272d 100%)}
.quote{left:442px;top:236px;width:568px;font-family:"Roboto",Arial,sans-serif;font-style:italic;font-weight:300;font-size:19px;line-height:1.55;color:var(--ink);text-align:right}
.name-bar{left:0;top:457px;width:1200px;height:77px;background:var(--green)}
.client-name{left:268px;top:12px;color:var(--white);font-family:"Roboto",Arial,sans-serif;text-align:left}
.client-name strong{display:block;font-weight:500;font-size:19px}
.client-name span{font-size:15px}
.slide-dots{left:668px;top:32px;display:flex;gap:5px}
.slide-dots span{width:13px;height:13px;border:1.5px solid var(--white)}
.slide-dots span.on{background:var(--white)}

/* partners */
.partners{top:2384px;height:286px}
.partners h2{left:190px;top:54px;font-size:33px}
.partners .lead{left:190px;top:102px;width:420px}
.partner{top:208px;font-family:"Roboto",Arial,sans-serif;font-weight:500;font-size:22px;color:#4c5257}

/* subscribe */
.subscribe{top:2670px;height:317px;background:linear-gradient(120deg,#5a5a55 0%,#7b7a72 45%,#56585a 100%)}
.subscribe h2{left:0;width:1200px;text-align:center;top:84px;font-size:32px;color:var(--white)}
.sub-form{left:400px;top:154px;display:flex}
.sub-input{width:258px;height:30px;background:var(--white);font-size:10px;color:var(--muted);padding:9px 10px}
.sub-button{width:121px;height:30px;background:var(--green);color:var(--white);font-family:"Roboto",Arial,sans-serif;font-size:12px;font-weight:500;display:flex;align-items:center;justify-content:center}
.sub-note{left:0;width:1200px;top:204px;text-align:center;font-size:10.5px;line-height:1.6;color:#d6d6d2}
.sub-note a{color:var(--green);text-decoration:none}

/* call to action */
.cta{top:2987px;height:158px;background:var(--green);color:var(--white)}
.cta h2{left:190px;top:42px;font-size:32px;font-weight:400;color:var(--white)}
.cta p{left:190px;top:92px;font-family:"Roboto",Arial,sans-serif;font-size:18px}

/* footer */
.site-footer{top:3145px;height:281px;background:var(--blue);color:#c8d6e8}
.foot-col{top:56px;font-size:9.5px;line-height:1.6}
.foot-col h4{font-family:"Roboto",Arial,sans-serif;font-weight:500;font-size:12px;color:var(--white);margin-bottom:16px}
.foot-col a{color:var(--green);text-decoration:none}
.post{margin-bottom:14px;display:flex;gap:6px}
.adviser-grid{display:grid;grid-template-columns:repeat(3,51px);gap:6px}
.adviser-grid div{height:51px;background:linear-gradient(180deg,#f2f4f6,#c9d3dc)}
.foot-col .btn{margin-top:10px;font-size:9px;padding:4px 12px}
.contact{display:flex;gap:12px;margin-bottom:14px;align-items:flex-start}
.socials{display:flex;gap:8px;margin-top:14px}
.socials span{width:9px;height:9px;border-radius:50%;background:#7ea3cc}

/* bottom bar */
.bottom-bar{top:3426px;height:62px;background:var(--white)}
.bottom-brand{left:200px;top:19px;display:flex;align-items:center;gap:12px;font-size:13px;color:var(--muted)}
.bottom-brand i{width:24px;height:24px;border-radius:50%;background:var(--green);display:block}
.bottom-brand b{font-family:"Roboto",Arial,sans-serif;font-weight:500;color:var(--ink);font-size:15px}
.bottom-nav{left:542px;top:24px;display:flex;gap:24px;font-family:"Roboto",Arial,sans-serif;font-size:10px;font-weight:500;color:var(--blue);text-transform:uppercase}
.to-top{left:990px;top:21px}
</style>
</head>
<body>

<header class="site-header">
  <div class="abs brand"><span class="brand-dot"></span>Lorvin medical</div>
  <nav class="abs main-nav">
    <a class="active" href="#">Home</a><a href="#">Fertility</a><a href="#">Pregnancy Basics</a><a href="#">Articles</a><a href="#">Tips and News</a>
  </nav>
  <div class="abs header-tools">
    <svg width="13" height="13" viewBox="0 0 13 13"><circle cx="5.5" cy="5.5" r="4.2" fill="none" stroke="#9aa0a4" stroke-width="1.5"/><line x1="8.6" y1="8.6" x2="12" y2="12" stroke="#9aa0a4" stroke-width="1.5"/></svg>
    <span class="tool-dot"></span><span class="tool-dot"></span><span class="tool-dot"></span>
  </div>
</header>

<section class="hero" role="img" aria-label="Photo of an expecting couple sitting together on a sofa at home">
  <div class="abs hero-card">
    <svg class="fold" width="46" height="40" viewBox="0 0 46 40"><polygon points="0,0 46,0 46,40" fill="#ffffff"/><polygon points="0,0 46,40 0,40" fill="#a6d46e"/></svg>
    <h1>Lorem ipsum dolor<br>sit amet dolor.</h1>
    <p>Lorem ipsum dolor sit amet, consectetur adipiscing elit.<br>Nam vestibulum nec ex feugiat congue.</p>
  </div>
  <svg class="abs hero-arrow" style="left:68px" width="16" height="30" viewBox="0 0 16 30"><polyline points="14,2 2,15 14,28" fill="none" stroke="#fff" stroke-width="2"/></svg>
  <svg class="abs hero-arrow" style="left:1118px" width="16" height="30" viewBox="0 0 16 30"><polyline points="2,2 14,15 2,28" fill="none" stroke="#fff" stroke-width="2"/></svg>
  <div class="abs hero-dots"><span class="on"></span><span></span><span></span><span></span><span></span></div>
</section>

<section class="welcome">
  <h2 class="abs">Welcome to <b>Lorvin medical</b></h2>
  <p class="abs lead">Lorem ipsum dolor sit amet, consectetur adipiscing elit. Sed ut est sit amet ex efficitur consequat <span class="accent">sed nec dui</span>. risque vestibulum.</p>
  <div class="abs trimester" style="left:190px">
    <div class="tri-num">1</div>
    <div><h3>First Trimester</h3><p>Lorem ipsum dolor sit amet, consectetur adipiscing elit. Sed ut est sit amet ex efficitur consequat sed nec dui.</p><a href="#">Learn More</a></div>
  </div>
  <div class="abs trimester" style="left:465px">
    <div class="tri-num alt">2</div>
    <div><h3>Second Trimester</h3><p>Lorem ipsum dolor sit amet, consectetur adipiscing elit. Sed ut est sit amet ex efficitur consequat sed nec dui.</p><a href="#">Learn More</a></div>
  </div>
  <div class="abs trimester" style="left:747px">
    <div class="tri-num">3</div>
    <div><h3>Third Trimester</h3><p>Lorem ipsum dolor sit amet, consectetur adipiscing elit. Sed ut est sit amet ex efficitur consequat sed nec dui.</p><a href="#">Learn More</a></div>
  </div>
</section>

<section class="feature">
  <div class="abs feature-photo" role="img" aria-label="Photo of a relaxed pregnant woman resting on a towel during a spa treatment"></div>
  <svg class="abs notch" width="24" height="14" viewBox="0 0 24 14"><polygon points="0,0 24,0 12,13" fill="#ffffff"/></svg>
  <div class="abs feature-card">
    <svg class="fold" width="66" height="46" viewBox="0 0 66 46"><polygon points="0,0 66,0 66,46" fill="#d9e6b4"/><polygon points="0,0 66,46 0,46" fill="#1a5aa2"/></svg>
    <h3>Second Trimester</h3>
    <p class="intro">Lorem ipsum dolor sit amet, consectetur adipiscing elit. Sed ut est sit amet ex efficitur consequat <span class="accent">sed nec dui</span>. ex feugiat placerat.</p>
    <p class="detail">Lorem ipsum dolor sit amet, consectetur adipiscing elit. Sed ut est sit amet ex efficitur consequat sed nec dui. Sed interdum vulputate ex feugiat placerat. Integer mauris enim, aliquet ut placerat in, luctus ac odio.</p>
    <span class="btn">Learn More</span>
  </div>
</section>

<section class="advisors">
  <h2 class="abs">Our Advisors</h2>
  <p class="abs lead">Lorem ipsum dolor sit amet, consectetur adipiscing elit. consequat <span class="accent">sed nec dui</span>. risque vestibulum.</p>
  <ul class="abs checklist">
    <li><svg width="10" height="8" viewBox="0 0 10 8"><polyline points="1,4 4,7 9,1" fill="none" stroke="#86c043" stroke-width="1.8"/></svg>Lorem <span class="accent">ipsum dolor</span> sit amet, consectetur adipiscing libero eget.</li>
    <li><svg width="10" height="8" viewBox="0 0 10 8"><polyline points="1,4 4,7 9,1" fill="none" stroke="#86c043" stroke-width="1.8"/></svg>Curabitur mattis nisl, eget sodales elit in.</li>
    <li><svg width="10" height="8" viewBox="0 0 10 8"><polyline points="1,4 4,7 9,1" fill="none" stroke="#86c043" stroke-width="1.8"/></svg>Ut scelerisque tempor enim at tincidunt. <span class="accent">Etiam et odio</span> at justo.</li>
    <li><svg width="10" height="8" viewBox="0 0 10 8"><polyline points="1,4 4,7 9,1" fill="none" stroke="#86c043" stroke-width="1.8"/></svg>Duis ut ipsum nibh dum.</li>
    <li><svg width="10" height="8" viewBox="0 0 10 8"><polyline points="1,4 4,7 9,1" fill="none" stroke="#86c043" stroke-width="1.8"/></svg>Lorem ipsum dolor sit amet, consectetur adipiscing.</li>
    <li><svg width="10" height="8" viewBox="0 0 10 8"><polyline points="1,4 4,7 9,1" fill="none" stroke="#86c043" stroke-width="1.8"/></svg>Sed fringilla lectus ut metus vulputate, non pellentesque lacus.</li>
  </ul>
  <span class="abs btn">Learn More</span>
  <div class="abs advisors-photo" role="img" aria-label="Photo of two smiling medical advisors, a nurse and a doctor with a stethoscope"></div>
</section>

<section class="feedback">
  <h2 class="abs">Client <span class="accent">Feedback</span> To Our Service</h2>
  <div class="abs client-photo" role="img" aria-label="Photo of a senior doctor in a suit giving a thumbs up"></div>
  <p class="abs quote">"Lorem ipsum dolor sit amet, <span class="accent">consectetur</span> adipiscing elit. Nam condimentum leo sed nisi malesuada, sed accumsan metus ultricies. Donec eleifend nibh in ultrices tempus. Morbi id tempor lorem. Suspendisse potenti. Fusce at augue pulvinar, ultricies nisl id, bibendum est. "</p>
  <div class="abs name-bar">
    <div class="abs client-name"><strong>Dr. Owen Farrow</strong><span>Pregnancy Experts</span></div>
    <div class="abs slide-dots"><span></span><span></span><span class="on"></span><span></span></div>
  </div>
</section>

<section class="partners">
  <h2 class="abs">Our Partners</h2>
  <p class="abs lead">Lorem ipsum dolor sit amet, consectetur adipiscing elit. consequat <span class="accent">sed nec dui</span>. risque vestibulum.</p>
  <div class="abs partner" style="left:190px">Carewell</div>
  <div class="abs partner" style="left:405px">Nearby</div>
  <div class="abs partner" style="left:561px">Ratewise</div>
  <div class="abs partner" style="left:719px">Findly</div>
  <div class="abs partner" style="left:872px">Townlist</div>
</section>

<section class="subscribe" role="img" aria-label="Dimmed photo of hands writing in a notebook beside a glass of water and a tablet">
  <h2 class="abs">Subscribe to get monthly news letter</h2>
  <div class="abs sub-form"><div class="sub-input">Your Email Address</div><div class="sub-button">Subscribe</div></div>
  <p class="abs sub-note">Lorem Ipsum is simply dummy text of the printing<br><a href="#">Privacy Policy</a></p>
</section>

<section class="cta">
  <h2 class="abs">The Best Solution For Healthy And Happy Pregnancy.</h2>
  <p class="abs">Lorem ipsum dolor sit amet, consectetur adipiscing elit. <span style="color:#1d4f8a">+1 555 014 2290</span></p>
</section>

<footer class="site-footer">
  <div class="abs foot-col" style="left:190px;width:190px">
    <h4>About Company</h4>
    <p>Lorem Ipsum is simply dummy text of the printing and typesetting industry. Lorem Ipsum has been the industry's standard dummy text ever since a type specimen book.</p>
    <p style="margin-top:10px"><a href="#">Read More</a></p>
    <div class="socials"><span></span><span></span><span></span></div>
  </div>
  <div class="abs foot-col" style="left:412px;width:185px">
    <h4>Recent Post</h4>
    <div class="post"><span>›</span><p>Lorem Ipsum is simply dummy text of the printing and typesetting: <span style="color:#fff">Today</span></p></div>
    <div class="post"><span>›</span><p><a href="#">Lorem Ipsum is simply</a>: <span style="color:#fff">Today</span></p></div>
    <div class="post"><span>›</span><p>Lorem Ipsum is simply dummy text of the and typesetting: <span style="color:#fff">Today</span></p></div>
    <div class="post"><span>›</span><p><a href="#">Lorem Ipsum is simply</a>: <span style="color:#fff">Today</span></p></div>
  </div>
  <div class="abs foot-col" style="left:626px">
    <h4>Our Advisers</h4>
    <div class="adviser-grid" role="img" aria-label="Grid of six small adviser portrait photos"><div></div><div></div><div></div><div></div><div></div><div></div></div>
    <span class="btn">See More</span>
  </div>
  <div class="abs foot-col" style="left:830px;width:190px">
    <h4>Contact Information</h4>
    <div class="contact"><svg width="10" height="13" viewBox="0 0 10 13"><path d="M5 0a5 5 0 0 0-5 5c0 3.5 5 8 5 8s5-4.5 5-8a5 5 0 0 0-5-5z" fill="#fff"/><circle cx="5" cy="5" r="1.8" fill="#0c4a8e"/></svg><p>48 Alder Lane, Springvale 0412<br>02714-226494</p></div>
    <div class="contact"><svg width="10" height="13" viewBox="0 0 10 13"><rect x="1" y="0" width="8" height="13" rx="1.5" fill="#fff"/><rect x="2.5" y="2" width="5" height="7" fill="#0c4a8e"/></svg><p>+15550147830<br>+15550149321</p></div>
    <div class="contact"><svg width="12" height="9" viewBox="0 0 12 9"><rect width="12" height="9" fill="#fff"/><polyline points="0,0 6,5 12,0" fill="none" stroke="#0c4a8e"/></svg><p><a href="#">hello@lorvinmed.test</a><br><a href="#">www.lorvinmed.test</a></p></div>
  </div>
</footer>

<div class="bottom-bar" style="position:absolute;left:0;width:1200px">
  <div class="abs bottom-brand"><i></i>© 2017 <b>Lorvin medical</b></div>
  <nav class="abs bottom-nav"><span>Home</span><span>Fertility</span><span>Pregnancy Basics</span><span>Articles</span><span>Tips and News</span></nav>
  <svg class="abs to-top" width="20" height="20" viewBox="0 0 20 20"><circle cx="10" cy="10" r="9" fill="none" stroke="#86c043" stroke-width="1.4"/><polyline points="6,12 10,8 14,12" fill="none" stroke="#86c043" stroke-width="1.4"/></svg>
</div>

</body>
</html>
```